BRIGHT PEAK POWER.

I'd like my business logo.
contact name: Daniel Fitzhume
phone:0407395182
email: info@brightpeakpower.net.au
website: www.brightpeakpower.net.au

services:
solar
battery storage
LED lighting
energy saving solutions
general electrical
I'd like the design to look professional

Target Market(s)

Everyone

Industry/Entity Type

Business

Contact Information for Business Card

as described above

Requirements
Must have
• Id like the colours and the design to work well with my logo.

```html
<!DOCTYPE html>
<html lang="en">
<head>
<meta charset="utf-8">
<title>Bright Peak Power – Business Card</title>
<link rel="stylesheet" href="https://fonts.googleapis.com/css2?family=Arimo:wght@400;700&display=swap">
<style>
  :root {
    --backdrop: #2b2b2b;
    --card: #ffffff;
    --card-edge: #e6e6e6;
    --orange: #e9a43c;
    --green: #3ba64a;
    --ink: #1e1e1e;
  }
  * { margin: 0; padding: 0; box-sizing: border-box; }
  html, body {
    width: 1200px; height: 997px; overflow: hidden;
    background: var(--backdrop);
    font-family: "Arimo", Arial, sans-serif;
  }
  .stage { position: relative; width: 1200px; height: 997px; }

  .card {
    position: absolute;
    width: 600px; height: 343px;
    background: linear-gradient(160deg, #ffffff 0%, #f4f4f4 100%);
    border-radius: 22px;
    box-shadow: 0 10px 30px rgba(0,0,0,.45);
  }
  .card--front { left: 300px; top: 90px; }
  .card--back  { left: 300px; top: 520px; }

  /* brand name */
  .brand {
    display: flex; align-items: center; gap: 12px;
    color: var(--green); font-weight: 700; letter-spacing: .5px;
  }
  .brand__dot { border-radius: 50%; background: var(--green); flex: none; }

  /* front */
  .front__brand {
    position: absolute; left: 50%; top: 50%;
    transform: translate(-50%, -50%);
    font-size: 30px; white-space: nowrap;
  }
  .front__brand .brand__dot { width: 34px; height: 34px; }
  .service {
    position: absolute; color: var(--orange);
    font-size: 15px; font-weight: 700; letter-spacing: 1.5px;
    white-space: nowrap;
  }
  .service--storage { left: 205px; top: 70px; }
  .service--solar   { right: 60px; top: 70px; }
  .service--led     { left: 42px; top: 240px; }
  .service--saving  { right: 48px; top: 240px; }

  /* back */
  .back__brand {
    position: absolute; right: 36px; top: 34px; font-size: 22px;
  }
  .back__brand .brand__dot { width: 26px; height: 26px; }
  .back__rule {
    position: absolute; left: 200px; right: 40px; top: 138px;
    height: 2px; background: var(--green);
  }
  .back__mark {
    position: absolute; right: 48px; top: 170px;
    width: 110px; height: 110px; border-radius: 50%;
    background: radial-gradient(circle, rgba(59,166,74,.28), rgba(233,164,60,.18));
  }
  .person { position: absolute; left: 40px; top: 122px; }
  .person__name { color: var(--green); font-size: 19px; font-weight: 700; }
  .person__role { color: var(--ink); font-size: 18px; margin-top: 2px; }

  .contacts {
    position: absolute; left: 40px; top: 200px;
    list-style: none;
  }
  .contacts li {
    display: flex; align-items: center; gap: 14px;
    color: var(--ink); font-size: 18px; margin-bottom: 16px;
  }
  .contacts svg { width: 16px; height: 16px; fill: var(--green); flex: none; }
</style>
</head>
<body>
<main class="stage">

  <section class="card card--front" aria-label="Card front">
    <span class="service service--storage">BATTERY STORAGE</span>
    <span class="service service--solar">SOLAR</span>
    <div class="brand front__brand"><span class="brand__dot"></span>BRIGHT PEAK POWER</div>
    <span class="service service--led">LED LIGHTING</span>
    <span class="service service--saving">ENERGY SAVING SOLUTIONS</span>
  </section>

  <section class="card card--back" aria-label="Card back">
    <div class="brand back__brand"><span class="brand__dot"></span>BRIGHT PEAK POWER</div>
    <div class="back__rule"></div>
    <div class="back__mark"></div>

    <div class="person">
      <p class="person__name">Daniel Fitzhume</p>
      <p class="person__role">Director</p>
    </div>

    <ul class="contacts">
      <li>
        <svg viewBox="0 0 16 16" aria-hidden="true"><path d="M3 1h3l1.5 4-2 1.2a9 9 0 0 0 4.3 4.3L11 8.5l4 1.5v3c0 1-1 2-2 2A13 13 0 0 1 1 3c0-1 1-2 2-2z"/></svg>
        0407395182
      </li>
      <li>
        <svg viewBox="0 0 16 16" aria-hidden="true"><path d="M1 3h14v10H1z M1.5 3.5 8 9l6.5-5.5" stroke="#fff" stroke-width="1.2"/></svg>
        info@brightpeakpower.net.au
      </li>
      <li>
        <svg viewBox="0 0 16 16" aria-hidden="true"><circle cx="8" cy="8" r="7"/><path d="M1 8h14M8 1c-3 3-3 11 0 14M8 1c3 3 3 11 0 14" stroke="#fff" stroke-width="1" fill="none"/></svg>
        www.brightpeakpower.net.au
      </li>
    </ul>
  </section>

</main>
</body>
</html>
```